Google slides for an upcoming presentation

I would like to recreate the jpeg to better match our company branding & color, as well as better resolution-- which is found in the PPTX. The slide should read....
"What are the biggest differences between Web 2.0 to Web 3.0"

Industry/Entity Type

Web3

Other font styles liked:
• Manrope

```html
<!DOCTYPE html>
<html lang="en">
<head>
<meta charset="UTF-8">
<title>Web 2.0 to Web 3.0</title>
<link rel="stylesheet" href="https://fonts.googleapis.com/css2?family=Manrope:wght@400;500;600;700&display=swap">
<style>
  :root {
    --bg: #ffffff;
    --ink: #0a0a0a;
    --on-badge: #ffffff;
    --web2-green: #58e594;
    --web3-orange: #f99f4a;
    --wave-pink: #f6a6d8;
    --wave-violet: #b98cf2;
    --wave-blue: #6d7cf0;
    --wave-cyan: #7fd9f2;
    --wave-peach: #f7b6a4;
  }
  * { margin: 0; padding: 0; box-sizing: border-box; }
  html, body {
    width: 1200px;
    height: 675px;
    overflow: hidden;
    background: var(--bg);
  }
  .slide {
    position: relative;
    width: 1200px;
    height: 675px;
    overflow: hidden;
    background: var(--bg);
    font-family: "Manrope", sans-serif;
    color: var(--ink);
  }
  .wave-field {
    position: absolute;
    left: 0;
    top: 120px;
    width: 1200px;
    height: 555px;
    background:
      linear-gradient(100deg,
        var(--wave-peach) 0%,
        var(--wave-pink) 14%,
        var(--wave-violet) 35%,
        var(--wave-blue) 58%,
        var(--wave-cyan) 100%);
    opacity: 0.22;
    -webkit-mask-image: linear-gradient(180deg, transparent 0%, #000 30%, #000 80%, transparent 100%);
            mask-image: linear-gradient(180deg, transparent 0%, #000 30%, #000 80%, transparent 100%);
  }
  .headline {
    position: absolute;
    left: 0;
    top: 52px;
    width: 1200px;
    text-align: center;
    font-size: 57px;
    font-weight: 400;
    letter-spacing: -0.5px;
    line-height: 1;
  }
  .badge {
    position: absolute;
    top: 196px;
    width: 350px;
    height: 402px;
  }
  .badge--web2 { left: 94px; }
  .badge--web3 { left: 755px; }
  .badge svg {
    position: absolute;
    inset: 0;
    width: 100%;
    height: 100%;
  }
  .badge__label {
    position: absolute;
    left: 0;
    width: 100%;
    text-align: center;
    color: var(--on-badge);
    line-height: 1;
  }
  .badge__word {
    top: 88px;
    font-size: 84px;
    font-weight: 700;
    letter-spacing: -1px;
  }
  .badge__version {
    top: 186px;
    font-size: 142px;
    font-weight: 500;
    letter-spacing: -2px;
  }
  .connector {
    position: absolute;
    left: 560px;
    top: 356px;
    width: 80px;
    text-align: center;
    font-size: 60px;
    font-weight: 400;
    line-height: 1;
  }
</style>
</head>
<body>
  <main class="slide">
    <div class="wave-field" role="img" aria-label="Flowing dotted wave pattern in peach, pink, violet, blue and cyan"></div>

    <h1 class="headline">What are the biggest differences between:</h1>

    <div class="badge badge--web2">
      <svg viewBox="0 0 350 402" aria-hidden="true">
        <polygon points="175,12 338,106 338,296 175,390 12,296 12,106"
                 fill="var(--web2-green)" stroke="var(--web2-green)"
                 stroke-width="22" stroke-linejoin="round"/>
      </svg>
      <span class="badge__label badge__word">Web</span>
      <span class="badge__label badge__version">2.0</span>
    </div>

    <p class="connector">to</p>

    <div class="badge badge--web3">
      <svg viewBox="0 0 350 402" aria-hidden="true">
        <polygon points="175,12 338,106 338,296 175,390 12,296 12,106"
                 fill="var(--web3-orange)" stroke="var(--web3-orange)"
                 stroke-width="22" stroke-linejoin="round"/>
      </svg>
      <span class="badge__label badge__word">Web</span>
      <span class="badge__label badge__version">3.0</span>
    </div>
  </main>
</body>
</html>
```